Copperfield Wire - Subscription Landing page

we need responsive landing page for a new news service about the Blockchain innovations coins and startups, the landing page includes vertical video player and call to action button, attach mockup.
temporary page
http://www.cpfw.io/
1 page

```html
<!DOCTYPE html>
<html lang="en">
<head>
<meta charset="utf-8">
<title>Copperfield Wire – Subscription Landing Page Variants</title>
<link href="https://fonts.googleapis.com/css2?family=Poppins:wght@400;600;700&display=swap" rel="stylesheet">
<style>
  :root {
    --page: #ffffff;
    --ink: #1a1a1a;
    --brand-red: #e3101f;
    --navy-deep: #0a1a33;
    --navy: #0d2a57;
    --blue: #0d5aa8;
    --cyan: #1ff0f0;
    --card-tint: #fde7e7;
    --phone-frame: #222428;
    --shape-light: rgba(230, 240, 250, 0.88);
  }
  * { box-sizing: border-box; margin: 0; padding: 0; }
  html, body { width: 1200px; height: 799px; overflow: hidden; background: var(--page); }
  body { position: relative; font-family: "Poppins", sans-serif; color: var(--ink); }

  .variant {
    position: absolute; width: 513px; height: 335px; overflow: hidden;
    box-shadow: 0 1px 4px rgba(0,0,0,0.18); background: var(--page);
  }
  .variant--a { left: 70px;  top: 44px; }
  .variant--b { left: 617px; top: 44px; }
  .variant--c { left: 70px;  top: 420px; }
  .variant--d { left: 617px; top: 420px; }

  .site-header { position: absolute; left: 0; top: 0; width: 100%; height: 46px; background: var(--page); }
  .brand { position: absolute; left: 48px; top: 14px; display: flex; align-items: center; gap: 6px; }
  .brand-mark { width: 18px; height: 18px; border-radius: 50%; background: var(--brand-red); }
  .brand-name { font-weight: 600; font-size: 14px; color: var(--brand-red); line-height: 1; }
  .tagline { position: absolute; left: 225px; top: 15px; font-weight: 700; font-size: 12.5px; letter-spacing: 0.1px; }

  .hero { position: absolute; left: 0; top: 46px; width: 100%; height: 289px; }
  .hero--bright { background: linear-gradient(225deg, var(--cyan) 0%, #1aa9d6 25%, var(--blue) 55%, var(--navy) 100%); }
  .hero--dark { background: radial-gradient(ellipse at 50% 40%, #123158 0%, var(--navy-deep) 75%); }

  .signup-card {
    position: absolute; left: 105px; top: 77px; width: 303px; height: 229px;
    border-radius: 24px; background: linear-gradient(135deg, var(--card-tint) 0%, #ffffff 55%);
  }

  .phone {
    position: absolute; width: 92px; height: 188px; border-radius: 14px;
    background: var(--phone-frame); padding: 4px;
  }
  .phone-screen {
    width: 100%; height: 100%; border-radius: 11px;
    background: linear-gradient(180deg, #3c4a66 0%, #7a6a68 40%, #e9d6cc 75%, #f2e4dc 100%);
  }
  .phone-notch { position: absolute; left: 30px; top: 4px; width: 32px; height: 6px; border-radius: 0 0 5px 5px; background: var(--phone-frame); }
  .play { position: absolute; left: 33px; top: 82px; width: 26px; height: 26px; }

  .pitch { position: absolute; text-align: center; }
  .pitch p { font-size: 8.6px; line-height: 14px; }
  .pitch h2 { font-weight: 700; font-size: 8.8px; line-height: 14.5px; margin-top: 9px; }
  .cta {
    display: inline-block; margin-top: 10px; padding: 0 14px; height: 17px; line-height: 17px;
    border-radius: 9px; background: var(--brand-red); color: #fff; font-weight: 600; font-size: 6.4px;
  }
  .channels { display: flex; justify-content: center; gap: 11px; margin-top: 15px; }
  .channel { width: 8px; height: 8px; border-radius: 50%; background: var(--ink); }

  .pitch--card { left: 96px; top: 35px; width: 225px; }

  .pitch--compact { width: 150px; }
  .pitch--compact p { font-size: 6.6px; line-height: 11.5px; }
  .pitch--compact h2 { font-size: 7px; line-height: 11.5px; margin-top: 7px; }
  .pitch--compact .cta { font-size: 5.2px; height: 14px; line-height: 14px; padding: 0 11px; margin-top: 8px; }
  .pitch--compact .channels { gap: 8px; margin-top: 10px; }
  .pitch--compact .channel { width: 6.5px; height: 6.5px; }
  .variant--d .pitch p, .variant--d .pitch h2 { color: #ffffff; }
  .variant--d .channel { background: #ffffff; }
</style>
</head>
<body>

<!-- Variant A: bright hero, card -->
<section class="variant variant--a">
  <header class="site-header">
    <div class="brand"><span class="brand-mark"></span><span class="brand-name">Copperfield Wire</span></div>
    <div class="tagline">BE READY FOR TOMORROW</div>
  </header>
  <div class="hero hero--bright" role="img" aria-label="Abstract glowing blockchain city of cubes and circuit lights"></div>
  <div class="signup-card">
    <div class="phone" style="left:25px;top:22px">
      <div class="phone-screen" role="img" aria-label="Vertical video of a presenter in front of a city skyline"></div>
      <div class="phone-notch"></div>
      <svg class="play" viewBox="0 0 26 26"><circle cx="13" cy="13" r="13" fill="#e3101f"/><path d="M10 8 L19 13 L10 18 Z" fill="#fff"/></svg>
    </div>
    <div class="pitch pitch--card">
      <p>Stay updated with all the latest<br>blockchain innovations coins and<br>startups in a daily video story.</p>
      <h2>SUBSCRIBE FOR FREE IN ONE OF<br>OUR CHANNELS BELOW:</h2>
      <span class="cta">BROWSER NOTIFICATION</span>
      <div class="channels"><span class="channel"></span><span class="channel"></span><span class="channel"></span><span class="channel"></span><span class="channel"></span></div>
    </div>
  </div>
</section>

<!-- Variant B: dark hero, card -->
<section class="variant variant--b">
  <header class="site-header">
    <div class="brand"><span class="brand-mark"></span><span class="brand-name">Copperfield Wire</span></div>
    <div class="tagline">BE READY FOR TOMORROW</div>
  </header>
  <div class="hero hero--dark" role="img" aria-label="Dark blue network of glowing cubes linked by dotted lines"></div>
  <div class="signup-card">
    <div class="phone" style="left:25px;top:22px">
      <div class="phone-screen" role="img" aria-label="Vertical video of a presenter in front of a city skyline"></div>
      <div class="phone-notch"></div>
      <svg class="play" viewBox="0 0 26 26"><circle cx="13" cy="13" r="13" fill="#e3101f"/><path d="M10 8 L19 13 L10 18 Z" fill="#fff"/></svg>
    </div>
    <div class="pitch pitch--card">
      <p>Stay updated with all the latest<br>blockchain innovations coins and<br>startups in a daily video story.</p>
      <h2>SUBSCRIBE FOR FREE IN ONE OF<br>OUR CHANNELS BELOW:</h2>
      <span class="cta">BROWSER NOTIFICATION</span>
      <div class="channels"><span class="channel"></span><span class="channel"></span><span class="channel"></span><span class="channel"></span><span class="channel"></span></div>
    </div>
  </div>
</section>

<!-- Variant C: bright hero, translucent pointer shape -->
<section class="variant variant--c">
  <header class="site-header">
    <div class="brand"><span class="brand-mark"></span><span class="brand-name">Copperfield Wire</span></div>
    <div class="tagline">BE READY FOR TOMORROW</div>
  </header>
  <div class="hero hero--bright" role="img" aria-label="Abstract glowing blockchain city of cubes and circuit lights"></div>
  <svg style="position:absolute;left:0;top:0" width="513" height="335" viewBox="0 0 513 335">
    <path d="M180,140 L325,96 Q378,80 378,132 L378,250 Q378,305 325,290 L180,248 Z" fill="var(--shape-light)"/>
  </svg>
  <div class="phone" style="left:148px;top:98px">
    <div class="phone-screen" role="img" aria-label="Vertical video of a presenter in front of a city skyline"></div>
    <div class="phone-notch"></div>
    <svg class="play" viewBox="0 0 26 26"><circle cx="13" cy="13" r="13" fill="#e3101f"/><path d="M10 8 L19 13 L10 18 Z" fill="#fff"/></svg>
  </div>
  <div class="pitch pitch--compact" style="left:226px;top:140px">
    <p>Stay updated with all the latest<br>blockchain innovations coins and<br>startups in a daily video story.</p>
    <h2>SUBSCRIBE FOR FREE IN ONE OF<br>OUR CHANNELS BELOW:</h2>
    <span class="cta">BROWSER NOTIFICATION</span>
    <div class="channels"><span class="channel"></span><span class="channel"></span><span class="channel"></span><span class="channel"></span><span class="channel"></span></div>
  </div>
</section>

<!-- Variant D: dark hero, outlined pointer shape -->
<section class="variant variant--d">
  <header class="site-header">
    <div class="brand"><span class="brand-mark"></span><span class="brand-name">Copperfield Wire</span></div>
    <div class="tagline">BE READY FOR TOMORROW</div>
  </header>
  <div class="hero hero--dark" role="img" aria-label="Dark blue network of glowing cubes linked by dotted lines"></div>
  <svg style="position:absolute;left:0;top:0" width="513" height="335" viewBox="0 0 513 335">
    <path d="M239,140 L325,96 Q378,80 378,132 L378,250 Q378,305 325,290 L239,248" fill="none" stroke="#ffffff" stroke-width="1"/>
  </svg>
  <div class="phone" style="left:148px;top:98px">
    <div class="phone-screen" role="img" aria-label="Vertical video of a presenter in front of a city skyline"></div>
    <div class="phone-notch"></div>
    <svg class="play" viewBox="0 0 26 26"><circle cx="13" cy="13" r="13" fill="#e3101f"/><path d="M10 8 L19 13 L10 18 Z" fill="#fff"/></svg>
  </div>
  <div class="pitch pitch--compact" style="left:232px;top:140px">
    <p>Stay updated with all the latest<br>blockchain innovations coins and<br>startups in a daily video story.</p>
    <h2>SUBSCRIBE FOR FREE IN ONE OF<br>OUR CHANNELS BELOW:</h2>
    <span class="cta">BROWSER NOTIFICATION</span>
    <div class="channels"><span class="channel"></span><span class="channel"></span><span class="channel"></span><span class="channel"></span><span class="channel"></span></div>
  </div>
</section>

</body>
</html>
```